Boutique Financial Services/Advisor Business Needs Web Design

Looking for an informational and functional web design for my Financial Services/Financial Advisement business. It should have functionality for Company name, address, phone #, "About Us", Who we are, Our Mission, Services we offer, Biographies/Photos of/about "The Team", and possibly a link to "Contact Us". Would like to see something new & exciting blended with a traditional/professional look that will appeal to those approaching retirement, as well as those younger clients that are beginning to think about planning for the future. I already have a web domain through Brixwell, but would like this to be the design we use for that domain.
Financial Services/Financial Advisor
Coded - Design and coding required
1 page

```html
<!DOCTYPE html>
<html lang="en">
<head>
<meta charset="utf-8">
<title>Halvorsen Wealth Partners</title>
<link rel="stylesheet" href="https://fonts.googleapis.com/css2?family=Poppins:ital,wght@0,400;0,500;0,600;1,600&display=swap">
<style>
:root{
  --blue:#1f66e0;
  --blue-deep:#2363d9;
  --blue-soft:#dfe9fb;
  --panel:#eaf1fc;
  --card:#e3ecfb;
  --ink:#111622;
  --dark:#1b2130;
  --muted:#4a5468;
  --white:#ffffff;
}
*{margin:0;padding:0;box-sizing:border-box}
html,body{width:1200px;height:4633px;overflow:hidden;background:var(--white)}
body{font-family:"Poppins",sans-serif;color:var(--ink);position:relative}
.abs{position:absolute}
.pill-dark{background:var(--dark);color:var(--white);border-radius:999px;display:flex;align-items:center;justify-content:center;font-weight:500}

/* hero */
.hero{left:27px;top:36px;width:1144px;height:731px;border-radius:36px;overflow:hidden;
  background:linear-gradient(180deg,#d9e6fb 0%,#8fb4f2 35%,#3f7fe8 70%,#2466de 100%)}
.brand{display:flex;align-items:center;gap:8px;font-size:12px;font-weight:500;color:#1c2a55}
.brand .dot{width:16px;height:16px;border-radius:50%;background:#1c2a55}
.hero .brand{left:41px;top:24px}
.menu{left:990px;top:23px;width:120px;height:44px;gap:12px;font-size:13px}
.menu .ic{width:30px;height:30px;border-radius:50%;border:1.5px solid #fff;display:flex;align-items:center;justify-content:center}
.headline{color:var(--white);font-weight:500;font-size:86px;line-height:1;letter-spacing:1px;white-space:nowrap}
.h1{top:92px;left:224px}
.h2{top:172px;left:405px;font-style:italic;font-weight:600}
.hero-sub{top:278px;left:360px;width:424px;text-align:center;color:#eef3ff;font-size:17px;line-height:21px}
.email{height:56px;width:366px;border-radius:999px;border:1.5px solid rgba(255,255,255,.85);
  background:rgba(255,255,255,.12);display:flex;align-items:center;justify-content:space-between;padding:0 6px 0 24px;color:#fff;font-size:17px}
.email .go{height:42px;width:124px;gap:8px;font-size:12px}
.email .go span.c{width:28px;height:28px;border-radius:50%;background:#3a4256;display:flex;align-items:center;justify-content:center}
.hero .email{left:399px;top:344px}
.photo{border-radius:14px 14px 0 0}
.ph-cash{left:34px;top:580px;width:337px;height:151px;background:linear-gradient(160deg,#8c9db0,#4e6277 60%,#2d3d52)}
.ph-chart{left:398px;top:450px;width:353px;height:281px;border-radius:16px 16px 0 0;background:linear-gradient(150deg,#1d3c7a,#3b73c8 45%,#9fbff0 60%,#19356e)}
.ph-coins{left:772px;top:580px;width:338px;height:151px;background:linear-gradient(160deg,#b7c7d9,#7d8fa5 50%,#4f6178)}
.stat{left:34px;top:499px;width:337px;height:77px;background:#fff;border-radius:18px;display:flex;align-items:center;padding:0 22px;gap:16px;font-size:17px;font-weight:500}
.stat .ic{width:32px;height:32px;border-radius:50%;background:var(--blue)}
.stat .tag{margin-left:auto;background:#bfe3c4;color:#1d5c2c;font-size:9px;padding:4px 10px;border-radius:999px}
.balance{left:772px;top:499px;width:338px;height:77px;background:rgba(255,255,255,.55);border-radius:18px;padding:8px}
.balance .in{height:61px;background:#e8f0fd;border-radius:14px;display:flex;align-items:center;gap:18px;padding:0 18px;font-size:27px}
.balance .in small{font-size:15px;color:#6a7489;font-style:italic}
.balance .ic{width:32px;height:32px;border-radius:50%;background:var(--blue)}

.trusted{top:800px;width:1200px;text-align:center;font-size:43px;font-weight:500}
.trusted b{color:var(--blue);font-weight:500}

/* about */
.about{left:52px;top:900px;width:1105px;height:635px;background:var(--panel)}
.about h2{position:absolute;top:48px;width:100%;text-align:center;font-size:54px;font-weight:500}
.tab{height:38px;border-radius:10px;display:flex;align-items:center;justify-content:center;font-size:12px}
.tab-mission{left:425px;top:175px;width:126px;background:#b3c8ee;color:#3d4f77}
.tab-who{left:564px;top:166px;width:145px;height:50px;background:var(--blue);color:#fff;box-shadow:0 4px 10px rgba(31,102,224,.35)}
.ph-about{left:69px;top:275px;width:460px;height:301px;border-radius:18px;background:radial-gradient(circle at 50% 50%,#2f7fd0,#123261 45%,#070f22 100%)}
.about p{position:absolute;left:565px;top:272px;width:515px;font-size:17.5px;line-height:27px;font-weight:500}
.read{left:565px;top:441px;width:121px;height:43px;font-size:18px}

/* values */
.sec-title{width:1200px;text-align:center;font-weight:500}
.values-title{top:1620px;font-size:32px}
.values-title b,.hl{color:var(--blue);font-weight:500}
.values-quote{top:1691px;font-size:18.5px}
.value{top:1776px;width:339px;height:442px;background:var(--card);border-radius:12px;padding:13px}
.value .img{height:293px;border-radius:8px}
.value h3{font-size:32px;font-weight:500;margin:14px 0 0 8px;line-height:1.1}
.value p{font-size:18.5px;font-weight:500;margin:4px 0 0 8px;line-height:27px}
.v1{left:92px}.v2{left:439px}.v3{left:787px}
.v1 h3,.v1 p{margin-left:28px}
.v1 .img{background:linear-gradient(180deg,#0f1c33,#1f3049 55%,#c8893a 80%,#28323f)}
.v2 .img{background:radial-gradient(circle at 30% 50%,#7ea6c9,#2b4a66 40%,#0e1b2b)}
.v3 .img{background:linear-gradient(180deg,#102a55,#3a84d8 55%,#dba16a 85%,#1c2640)}

/* services */
.services-title{left:92px;top:2318px;font-size:56px;font-weight:500}
.services-lead{left:99px;top:2418px;width:380px;font-size:18.5px;line-height:27px;font-weight:500}
.explore{left:92px;top:2516px;width:194px;height:44px;font-size:18px}
.acc{left:569px;width:541px;border:2px solid var(--blue);border-radius:4px;padding:0 30px;font-size:18.5px;font-weight:500;display:flex;align-items:center;justify-content:space-between}
.acc svg{flex:none}
.acc.closed{height:83px}
.acc.open{height:128px;top:2522px;background:var(--blue);color:#fff;flex-direction:column;align-items:stretch;justify-content:flex-start;padding-top:20px}
.acc.open .row{display:flex;justify-content:space-between;align-items:center}
.acc.open p{font-size:13px;font-weight:400;margin-top:26px}

/* team */
.team-title{top:3028px;font-size:58px}
.team-text{top:3126px;left:290px;width:620px;text-align:center;font-size:18.5px;line-height:27px;font-weight:500}
.team-learn{top:3191px;font-size:12px}
.click{left:571px;top:3231px;width:127px;height:43px;font-size:18px}
.member{height:40px;border-radius:999px;background:var(--card);box-shadow:0 3px 8px rgba(30,60,120,.15);font-size:12.5px;display:flex;align-items:center;justify-content:center;white-space:nowrap}
.lead-card{left:477px;top:3343px;width:315px;height:226px;background:#fff;border-radius:12px;box-shadow:0 4px 16px rgba(30,60,120,.18)}
.lead-name{position:absolute;left:0;top:0;width:315px;height:68px;border-radius:12px;box-shadow:0 3px 8px rgba(30,60,120,.12);display:flex;align-items:center;justify-content:center;font-size:13px;font-weight:600}
.lead-quote{position:absolute;left:11px;top:86px;width:293px;height:130px;background:var(--card);border-radius:14px;padding:20px 22px;font-size:13.5px;line-height:22px}

/* cta */
.cta{left:27px;top:3690px;width:1144px;height:527px;border-radius:36px;overflow:hidden;
  background:linear-gradient(180deg,#dbe7fb 0%,#8fb4f2 35%,#3f7fe8 72%,#2466de 100%)}
.cta h2{position:absolute;top:103px;width:100%;text-align:center;font-size:47px;line-height:65px;font-weight:500;color:rgba(255,255,255,.85)}
.cta .email{left:394px;top:331px}

/* footer */
.disclaimer{left:59px;top:4268px;width:330px;font-size:12px;line-height:18px}
.foot-brand{left:122px;top:4420px}
.foot-nav{left:455px;top:4276px;list-style:none;font-size:18.5px;line-height:43px}
.foot-nav li:first-child{font-weight:600}
.contact{left:612px;top:4276px;font-size:18.5px;line-height:24px}
.contact h4{font-weight:600;font-size:18.5px;margin-left:47px;margin-bottom:18px}
.contact .line{display:flex;gap:22px;margin-bottom:18px}
.contact .line span.ic{width:26px;height:26px;flex:none}
.social{left:972px;top:4274px}
.social h4{font-weight:600;font-size:18.5px;margin:0 0 16px 24px}
.social .row{display:flex;gap:14px}
.social .c{width:44px;height:44px;border-radius:50%;background:var(--dark);border:3px solid #b9c9e6}
.bottom{left:27px;top:4543px;width:1144px;height:69px;background:#d2e0f7;border-radius:20px 20px 0 0;display:flex;align-items:center;justify-content:center;font-size:13px}
</style>
</head>
<body>

<section class="hero abs">
  <div class="brand abs"><span class="dot"></span>HALVORSEN WEALTH</div>
  <div class="menu pill-dark abs"><span class="ic"><svg width="14" height="14" viewBox="0 0 14 14" fill="none" stroke="#fff" stroke-width="1.5"><rect x="1" y="1" width="5" height="5" rx="1"/><rect x="8" y="1" width="5" height="5" rx="1"/><rect x="1" y="8" width="5" height="5" rx="1"/><rect x="8" y="8" width="5" height="5" rx="1"/></svg></span>Menu</div>
  <div class="headline h1 abs">YOUR FUTURE</div>
  <div class="headline h2 abs">START HERE</div>
  <p class="hero-sub abs">Helping you achieve your financial goals with trusted solutions</p>
  <div class="email abs">Your Email Address<span class="go pill-dark"><span class="c"><svg width="12" height="12" viewBox="0 0 12 12"><path d="M2 1l8 4-3.5 1L5 10z" fill="#fff"/></svg></span>Get Started</span></div>
  <div class="photo ph-cash abs" role="img" aria-label="Stack of banknotes"></div>
  <div class="ph-chart abs" role="img" aria-label="Rising arrow over financial chart"></div>
  <div class="photo ph-coins abs" role="img" aria-label="Pile of coins"></div>
  <div class="stat abs"><span class="ic"></span>+10k<span class="tag">user</span></div>
  <div class="balance abs"><div class="in"><span class="ic"></span>$3,050.00 <small>USD</small></div></div>
</section>

<h2 class="trusted abs">Trusted By More Than <b>+10,000</b> Users</h2>

<section class="about abs">
  <h2>ABOUT US</h2>
  <div class="tab tab-mission abs">Our Mission</div>
  <div class="tab tab-who abs">Who We Are ?</div>
  <div class="ph-about abs" role="img" aria-label="Glowing dollar sign surrounded by orbit rings"></div>
  <p>Halvorsen Wealth Partners is a trusted financial consulting firm dedicated to helping businesses and individuals secure their financial futures. With decades of experience, we provide tailored strategies to achieve your goals with transparency, trust, and care.</p>
  <div class="read pill-dark abs">read more</div>
</section>

<h2 class="sec-title values-title abs">Our <b>Values</b></h2>
<p class="sec-title values-quote abs">"Guided by trust, driven by transparency, rooted in care."</p>

<article class="value v1 abs"><div class="img" role="img" aria-label="City skyline with golden light"></div><h3>Trust</h3><p>Your success is our priority.</p></article>
<article class="value v2 abs"><div class="img" role="img" aria-label="Digital globe with network lines"></div><h3>Transparency</h3><p>Clear guidance every step of the way.</p></article>
<article class="value v3 abs"><div class="img" role="img" aria-label="Illuminated city at night"></div><h3>Care</h3><p>Dedicated support for your unique needs.</p></article>

<h2 class="services-title abs">OUR <span class="hl">SERVICES</span></h2>
<p class="services-lead abs">Ready to take control of your financial future?</p>
<div class="explore pill-dark abs">Explore all Services</div>

<div class="acc closed abs" style="top:2414px">Financial Planning<svg width="18" height="10" viewBox="0 0 18 10" fill="none" stroke="#1f66e0" stroke-width="2"><path d="M2 2l7 6 7-6"/></svg></div>
<div class="acc open abs"><div class="row">Investment Management<svg width="18" height="10" viewBox="0 0 18 10" fill="none" stroke="#fff" stroke-width="2"><path d="M2 8l7-6 7 6"/></svg></div><p>Maximizing your returns while minimizing risks.</p></div>
<div class="acc closed abs" style="top:2675px">Retirement Planning<svg width="18" height="10" viewBox="0 0 18 10" fill="none" stroke="#1f66e0" stroke-width="2"><path d="M2 2l7 6 7-6"/></svg></div>
<div class="acc closed abs" style="top:2783px">Tax Advisory<svg width="18" height="10" viewBox="0 0 18 10" fill="none" stroke="#1f66e0" stroke-width="2"><path d="M2 2l7 6 7-6"/></svg></div>
<div class="acc closed abs" style="top:2891px">Small Business Support<svg width="18" height="10" viewBox="0 0 18 10" fill="none" stroke="#1f66e0" stroke-width="2"><path d="M2 2l7 6 7-6"/></svg></div>

<h2 class="sec-title team-title abs">OUR <span class="hl">TEAM</span></h2>
<p class="team-text abs">Our team of seasoned professionals brings years of experience and expertise to deliver exceptional results.</p>
<p class="sec-title team-learn abs">Learn more about our team ?</p>
<div class="click pill-dark abs">Click here</div>

<div class="member abs" style="left:104px;top:3371px;width:180px">Elise, Senior Financial</div>
<div class="member abs" style="left:234px;top:3479px;width:173px">Tomas, Senior Account</div>
<div class="member abs" style="left:868px;top:3371px;width:252px">Clara Voss, Senior Financial Advisor</div>
<div class="member abs" style="left:856px;top:3474px;width:234px">Owen Marlowe, Investment Strategist</div>
<div class="lead-card abs">
  <div class="lead-name">Daniel Reyes, CEO &amp; Founder</div>
  <svg class="abs" style="left:268px;top:48px" width="34" height="30" viewBox="0 0 34 30" fill="none" stroke="#1b2130" stroke-width="2"><path d="M14 10l14 6-6 2-2 6z" fill="#1b2130"/><path d="M8 4l3 3M4 12h4M14 2v4M6 20l3-3"/></svg>
  <p class="lead-quote">"With over 20 years in financial consulting, Daniel specializes in crafting comprehensive strategies for long-term growth."</p>
</div>

<section class="cta abs">
  <h2>Take control of your financial<br>future—schedule a consultation<br>today!</h2>
  <div class="email abs">Your Email Address<span class="go pill-dark"><span class="c"><svg width="12" height="12" viewBox="0 0 12 12"><path d="M2 1l8 4-3.5 1L5 10z" fill="#fff"/></svg></span>Get Started</span></div>
</section>

<footer>
  <p class="disclaimer abs">Halvorsen Wealth Partners provides financial consulting services and does not guarantee future investment performance. Please consult a licensed advisor for specific recommendations.</p>
  <div class="brand foot-brand abs"><span class="dot"></span>HALVORSEN WEALTH</div>
  <ul class="foot-nav abs"><li>Home</li><li>About Us</li><li>Our Services</li><li>Our Team</li><li>Contact Us</li></ul>
  <div class="contact abs">
    <h4>Contact Information</h4>
    <div class="line"><span class="ic"><svg width="26" height="26" viewBox="0 0 26 26"><circle cx="13" cy="13" r="12" fill="#1f66e0"/><path d="M13 6a5 5 0 0 0-5 5c0 4 5 9 5 9s5-5 5-9a5 5 0 0 0-5-5z" fill="#fff"/><circle cx="13" cy="11" r="2" fill="#1f66e0"/></svg></span><span>48 Halvorsen Way, Suite 400,<br>Anytown, USA</span></div>
    <div class="line"><span class="ic"><svg width="26" height="26" viewBox="0 0 26 26"><path d="M6 3l5 1 2 5-3 2a12 12 0 0 0 5 5l2-3 5 2 1 5c-1 2-3 3-5 3C10 23 3 16 3 8c0-2 1-4 3-5z" fill="#1f66e0"/></svg></span><span>(555) 014-2290</span></div>
    <div class="line"><span class="ic"><svg width="26" height="26" viewBox="0 0 26 26"><circle cx="13" cy="13" r="12" fill="#1f66e0"/><rect x="7" y="9" width="12" height="9" rx="1.5" fill="#fff"/><path d="M7 10l6 4 6-4" fill="none" stroke="#1f66e0" stroke-width="1.4"/></svg></span><span>contact@halvorsenwp.com</span></div>
  </div>
  <div class="social abs">
    <h4>Social Media</h4>
    <div class="row"><span class="c" aria-label="Professional network"></span><span class="c" aria-label="Social page"></span><span class="c" aria-label="Video channel"></span></div>
  </div>
  <div class="bottom abs">© 2024 Halvorsen Wealth Partners. All Rights Reserved.</div>
</footer>

</body>
</html>
```